Keglow Supply sales flyer for the licensed trade tri fold a4 leaflet style

Looking for a flyer / brochure to advertise our company service, needs to be modern and eye catching, aimed at licensee's and publicans. Our company saves them money on their beer losses.
I have attached some pictures which we use and our logo.
I have also attached leaflet that our parent company uses which contains more information.
Here are some key points
We are the originators of the specialist extended line cleaning service.
Our unique service allows for line cleaning to be extended from once every 7 days to once every 21 days.
We have provided our unique service since 1994
We guarantee our customers a minimum saving of 40% on their losses.
We are the only company to have been tested and proved by Tapwell and Brandt to improve quality and reduce costs.
Our web address is www.keglowsupplyuk.example if you need info.
Updates

Industry/Entity Type

It Company

Font styles to use
Sans Serif

Colors
fbee3d
ffffff
fece3e
fbed22
fbf289

Requirements
Must have
• We are the originators of the specialist extended line cleaning service.
• Our unique service allows for line cleaning to be extended from once every 7 days to once every 21 days.
• We have provided our unique service since 1994
• We guarantee our customers a minimum saving of 40% on their losses.
• We are the only company to have been tested and proved by Tapwell and Brandt to improve quality and reduce costs.

```html
<!DOCTYPE html>
<html lang="en">
<head>
<meta charset="utf-8">
<title>Keglow Supply – Tri-fold Leaflet</title>
<link rel="stylesheet" href="https://fonts.googleapis.com/css2?family=Questrial&family=Open+Sans:wght@400;600;700&family=Roboto+Slab:wght@400;700&family=Oswald:wght@500&display=swap">
<style>
:root{
  --page:#d9d9d9;
  --dark:#2b221d;
  --dark-2:#1f1915;
  --yellow:#fece3e;
  --bright:#fbed22;
  --pale:#fbf289;
  --red:#8e1518;
  --white:#ffffff;
  --muted:#cfc7bf;
}
*{margin:0;padding:0;box-sizing:border-box}
html,body{width:900px;height:1200px;overflow:hidden}
body{background:var(--page);font-family:"Open Sans",sans-serif;position:relative}
.sheet{position:absolute;left:88px;width:738px;background:var(--dark);overflow:hidden}
.sheet--outside{top:66px;height:522px}
.sheet--inside{top:621px;height:524px}
.abs{position:absolute}
.photo{position:absolute}
.fold{position:absolute;top:0;bottom:22px;width:1px;background:rgba(255,255,255,.08)}

/* outside */
.footer-band{position:absolute;left:0;right:0;bottom:0;height:22px;background:var(--bright);display:flex}
.footer-band span{flex:1;text-align:center;font:600 10px/22px "Open Sans",sans-serif;color:var(--dark-2)}
.cover-headline{left:28px;top:30px;font:400 25px/1.1 "Questrial",sans-serif;color:var(--white)}
.cover-headline em{font-style:normal;color:var(--yellow)}
.promise-list{left:28px;top:104px;border-left:2px solid var(--yellow);padding-left:12px;list-style:none}
.promise-list li{font:17px/26px "Questrial",sans-serif;color:var(--yellow)}
.guarantee{left:28px;top:200px;width:210px;font:13px/1.3 "Questrial",sans-serif;color:var(--white);white-space:nowrap}
.guarantee .big{font-size:18px;line-height:1.2}
.guarantee strong{color:var(--yellow);font-weight:400}
.since{left:28px;top:266px;width:204px;border-top:1px solid var(--yellow);padding-top:3px;font:700 7.6px "Open Sans",sans-serif;color:var(--yellow);white-space:nowrap}
.wordmark{font:700 13px "Questrial",sans-serif;color:var(--dark-2);display:flex;align-items:center;gap:6px}
.wordmark i{display:block;width:10px;height:10px;border-radius:50%;background:var(--yellow)}
.wordmark--small{color:var(--muted);font-size:10px}
.contact{left:245px;width:246px;top:370px;text-align:center;font:10.5px/1.35 "Open Sans",sans-serif;color:var(--muted)}
.contact .web{margin-top:14px}
.improved{left:492px;width:246px;top:327px;text-align:center;color:var(--white);font:700 18px/1.1 "Roboto Slab",serif}
.improved b{color:var(--yellow)}
.improved span{font:400 18px "Questrial",sans-serif}
.only{left:492px;width:246px;top:385px;text-align:center;font:500 10.5px/1.3 "Oswald",sans-serif;color:var(--white)}
.only b{color:var(--yellow);font-weight:500}
.savings-badge{left:516px;top:428px;width:194px;height:50px;border:1.5px solid var(--white);border-radius:12px;display:flex;align-items:center;justify-content:center;gap:8px}
.savings-badge .pct{font:34px "Questrial",sans-serif;color:var(--white)}
.savings-badge .lbl{font:17px/0.95 "Questrial",sans-serif;color:var(--yellow)}
.savings-badge .lbl b{font:600 12px "Open Sans",sans-serif;display:block}

/* inside */
.col{position:absolute;top:26px;font:7.3px/1.45 "Open Sans",sans-serif;color:var(--muted);text-align:justify}
.col p{margin-bottom:7px}
.col--left{left:22px;width:204px}
.col--mid{left:264px;width:204px;top:40px}
.col--mid p{border-bottom:1px solid rgba(255,255,255,.15);padding-bottom:7px;margin-bottom:8px}
.col--right{left:508px;width:212px}
.pill{display:inline-block;background:var(--yellow);color:var(--dark-2);font:400 13px "Roboto Slab",serif;border-radius:9px;padding:1px 10px;margin-bottom:8px}
.dots{list-style:none}
.dots li{position:relative;padding-left:12px;margin-bottom:7px}
.dots li::before{content:"";position:absolute;left:0;top:3px;width:5px;height:5px;border-radius:50%;background:var(--yellow)}
.divider{border-top:1px solid rgba(255,255,255,.15);margin:6px 0 8px}
.why{font:400 22px/1.1 "Questrial",sans-serif;color:var(--yellow);margin-bottom:18px;text-align:left}
.why span{color:var(--white)}
.report{font-weight:700;color:var(--white);font-size:8px}
</style>
</head>
<body>

<section class="sheet sheet--outside" aria-label="Leaflet outside">
  <div class="photo" style="left:0;top:297px;width:245px;height:203px;background:radial-gradient(circle at 40% 60%,#b4521f,#5a2a10 55%,#1e140e)" role="img" aria-label="Pint of amber beer being poured from a tap"></div>
  <div class="photo" style="left:245px;top:0;width:247px;height:310px;background:linear-gradient(180deg,#2f2626 0%,#5a4642 45%,#c9a25a 80%,#e8c23a 100%)" role="img" aria-label="Row of chrome beer taps at a bar"></div>
  <div class="photo" style="left:492px;top:0;width:246px;height:310px;background:linear-gradient(180deg,#ffffff 0%,#fdf6dc 45%,#fbe27a 75%,#f3b81f 100%)" role="img" aria-label="Bright golden beer bubbles"></div>
  <svg class="abs" style="left:245px;top:250px" width="493" height="80" viewBox="0 0 493 80">
    <path d="M0 45 Q250 -5 493 10 L493 80 L0 80Z" fill="#2b221d"/>
    <path d="M0 28 Q250 -10 493 0 L493 14 Q250 8 0 48Z" fill="#8e1518"/>
    <path d="M0 48 Q250 8 493 14 L493 18 Q250 14 0 54Z" fill="#fece3e"/>
  </svg>
  <div class="fold" style="left:245px"></div>
  <div class="fold" style="left:492px;top:40px;bottom:40px"></div>

  <h1 class="abs cover-headline">7 DAYS <em>TO ONCE</em><br><em>EVERY</em> 21 DAYS</h1>
  <ul class="abs promise-list"><li>NO CONTRACTS!</li><li>NO UPFRONT COSTS!</li><li>NO RENTAL COSTS!</li></ul>
  <p class="abs guarantee">WE GUARANTEE OUR CUSTOMERS<br><span class="big">A MINIMUM SAVING OF<br><strong>40%</strong> ON THEIR LOSSES</span></p>
  <p class="abs since">WE HAVE PROVIDED OUR UNIQUE SERVICE SINCE 1994</p>

  <div class="abs wordmark wordmark--small" style="left:318px;top:312px"><i></i>Keglow Supply (UK)</div>
  <div class="abs contact">
    <p>For further information or to arrange<br>a free survey and quotation<br>please contact<br>Tel 01632 96 02 62</p>
    <p class="web">www.keglowsupplyuk.example<br>info@keglowsupply.example</p>
  </div>

  <div class="abs wordmark" style="left:545px;top:80px;font-size:15px"><i></i>Keglow Supply (UK)</div>
  <h2 class="abs improved"><b>IMPROVED QUALITY</b><br><span>AND REDUCED COSTS</span></h2>
  <p class="abs only"><b>THE ONLY 3 WEEKLY LINE CLEANING SERVICE</b><br>proved by Brandt Brewers, Tapwell and the BQRI</p>
  <div class="abs savings-badge"><span class="pct">40%</span><span class="lbl">SAVINGS<b>GUARANTEED</b></span></div>

  <div class="footer-band"><span>www.keglowsupplyuk.example</span><span>www.keglowsupplyuk.example</span><span>www.keglowsupplyuk.example</span></div>
</section>

<section class="sheet sheet--inside" aria-label="Leaflet inside">
  <div class="photo" style="left:297px;top:240px;width:175px;height:140px;background:radial-gradient(circle at 50% 60%,#a8451c,#4a2410 60%,#2b221d)" role="img" aria-label="Glass of amber beer under a tap"></div>
  <div class="photo" style="left:0;top:350px;width:738px;height:174px;background:linear-gradient(90deg,#a88a62,#6d5236 30%,#8f7a60 55%,#3c2c20 75%,#b7a27a)" role="img" aria-label="Pub bar interior with beer pumps and spirit bottles"></div>
  <svg class="abs" style="left:0;top:318px" width="738" height="80" viewBox="0 0 738 80">
    <path d="M0 0 L738 0 L738 40 Q360 80 0 20Z" fill="#2b221d" fill-opacity="0"/>
    <path d="M0 20 Q360 80 738 40 L738 52 Q360 92 0 40Z" fill="#8e1518"/>
    <path d="M0 40 Q360 92 738 52 L738 58 Q360 98 0 48Z" fill="#ffffff"/>
  </svg>
  <div class="fold" style="left:245px;bottom:180px"></div>
  <div class="fold" style="left:492px;bottom:180px"></div>

  <div class="col col--left">
    <span class="pill">QUALITY ASSURED</span>
    <ul class="dots">
      <li>Our service has been designed to provide huge savings for our customers whilst providing them with the best quality product.</li>
      <li>Since 1994 customer satisfaction is the reason we are able to continue to provide our service.</li>
      <li>We have been independently tested by laboratories and trade organisations including the BQRI (Brewing Quality Research Institute) and proved by Tapwell, the largest technical service company in the UK and Brandt Brewers.</li>
    </ul>
    <span class="pill">ABOUT US</span>
    <p>We are the originators of the extended beer line cleaning and cellar maintenance service which we have provided since 1994.</p>
    <div class="divider"></div>
    <p>We are part of the Halden Group, the largest specialist organisation in the UK cleaning hundreds of thousands of beer lines each year.</p>
    <div class="divider"></div>
    <p>Our service is carried out by brewery trained technicians who have then been trained by ourselves to use our unique chemicals and equipment.</p>
  </div>

  <div class="col col--mid">
    <p>We manufacture our own range of Magnetic yeast inhibitors, which prevent the excess negative ions and sediments in beer settling on the lines.</p>
    <p>Our chemists designed and developed our unique chemicals to work specifically to our requirements. We use a two stage chemical process to ensure absolute line cleanliness.</p>
    <p>To ensure the correct mix of chemicals we developed an Auto-mix system which guarantees the perfect mix every time.</p>
    <p>The use of our unique chemicals, yeast inhibitors and our Auto-mix system guarantees a perfect pint every time and allows us to extend the requirement for line cleaning from once every 7 days to once every 21 days.</p>
    <p style="border:0">We guarantee to save our customers 40% of their existing weekly cleaning losses.</p>
  </div>

  <div class="col col--right">
    <h2 class="why">WHY KEGLOW<br><span>SUPPLY (UK) ?</span></h2>
    <ul class="dots">
      <li>We are the originators of the extended beer line cleaning and cellar maintenance service which we have provided since 1994.</li>
      <li>Our service has been tested and proved to work on all brewery dispense products.</li>
      <li>We are the only service to have been tested by Brandt brewers, Tapwell and the BQRI.</li>
      <li>We guarantee our customers total satisfaction, we do not ask them to sign a contract or make any upfront payments or rental agreements.</li>
      <li>We guarantee our customers a minimum of 40% savings on their existing weekly cleaning losses.</li>
      <li>We save our customers a minimum of 150 hours work per year by providing our service for them.</li>
      <li>Our technicians carry out a series of preventative maintenance service checks during our visits, to ensure the correct operation of the cellar and dispense equipment.</li>
    </ul>
    <p class="report">They then provide a written report</p>
  </div>
</section>

</body>
</html>
```